Mortgage firm needs clean and simple wordpress website and logo

The competition is for design only, and the winning design for the homepage will be expected to create a second design for a simpler template for additional pages.

We need a logo and basic wordpress website design for a Sydney based mortgage firm.
We need a clean and simple logo and website, based on the mortgage/accounting/finance/tax industry. Simple, credible and official colors.

The logo is expected to be so simple that we have combined into the one job.
If you submit a logo design and we choose it along with someone else's website design you will be paid a bonus of $60. The website design will still win the competition as per normal.

Current website is old and terrible but gives you an idea of the sitemap (super simple) and what they do: http://www.lendbridgeloans.com.au/

We will integrate a mortgage calculator into the site.
The calculator is adjustable in styles, you can see it here: http://www.lendbridgeloans.com.au/mortgagecalculator/

We want original different to copy-and-paste template looking designs.
We like simple websites with a long home page and a few additional pages like https://www.homefundpath.com.au/

We are based in Sydney Australia and are mortgage brokers

We want a clean, formal, credible site, limited pages.

The project is guaranteed, so go for it.

Example of basic template after home page complete: http://lendbridgeloans.com.au/template_example.jpg

Target Market(s)

Mortgage and banking clients

Industry/Entity Type

Finance

Number of Pages Required

1 page

Requirements
Must have
• A simple logo, Wordpress capable, be able to incorporate the mortgage calculator (on the home page if needed as well as its own page)
Nice to have
• VIdeo - something free but nice

```html
<!DOCTYPE html>
<html lang="en">
<head>
<meta charset="utf-8">
<title>Northgate Lending – Private Funding</title>
<link rel="stylesheet" href="https://fonts.googleapis.com/css2?family=Open+Sans:wght@400;600;700&family=Roboto:wght@400;500;700&display=swap">
<style>
:root{
  --orange:#e8661c;
  --slate:#464b53;
  --slate-dark:#3c4047;
  --ink:#1a1a1a;
  --text:#333;
  --muted:#888;
  --line:#cfcfcf;
  --white:#fff;
  --black:#000;
}
*{box-sizing:border-box;margin:0;padding:0}
html,body{width:1200px;height:3557px;overflow:hidden}
body{position:relative;background:var(--slate);font-family:"Open Sans",Arial,sans-serif;color:var(--text)}
.abs{position:absolute}
.btn{position:absolute;background:var(--orange);color:var(--white);font-family:"Roboto",Arial,sans-serif;font-size:13px;text-align:center;border-radius:3px;letter-spacing:.5px;white-space:nowrap}

/* header */
.site-header{left:0;top:0;width:1200px;height:47px;background:var(--white)}
.brand{font-family:"Roboto",Arial,sans-serif;font-weight:700;color:var(--orange);font-size:28px;line-height:1;white-space:nowrap}
.site-header .brand{left:62px;top:8px}
.search{left:346px;top:9px;width:359px;height:29px;border:1px solid #999;font-size:13px;color:#aaa;padding:6px 14px}
.nav-login{left:771px;top:14px;font-family:"Roboto",sans-serif;font-size:14px;color:var(--ink)}
.nav-menu{left:870px;top:14px;font-family:"Roboto",sans-serif;font-size:14px;color:var(--orange);display:flex;align-items:center;gap:6px}

/* sidebar */
.sidebar{left:975px;top:47px;width:225px;height:3510px;background:var(--black)}
.side-head{left:21px;font-family:"Roboto",sans-serif;font-size:15px;color:var(--orange);font-weight:500}
.side-link{left:21px;font-size:14px;color:#ddd}

/* hero card */
.hero-card{left:28px;top:47px;width:918px;height:1187px;background:var(--white)}
.contact-line{left:33px;font-size:14px;color:var(--ink)}
.hero-media{left:0;top:95px;width:918px;height:598px;background:linear-gradient(100deg,#fdfdfd 0%,#eef0f3 40%,#d8cbb0 62%,#c6a15a 80%,#9aa4b0 100%)}
.hero-rule{left:31px;top:180px;width:80px;height:3px;background:var(--orange)}
.hero-title{left:117px;top:176px;font-family:"Roboto",sans-serif;font-weight:700;font-size:34px;color:var(--orange);white-space:nowrap}
.hero-sub{left:117px;top:214px;font-family:"Roboto",sans-serif;font-size:28px;color:var(--orange)}
.hero-copy{left:176px;top:285px;width:300px;font-size:14px;line-height:24px;color:var(--ink)}
.section-title{font-family:"Roboto",sans-serif;font-weight:700;font-size:30px;color:var(--ink)}
.principle{top:820px;width:260px;text-align:center}
.principle h3{margin-top:18px;font-family:"Roboto",sans-serif;font-size:22px;font-weight:500;color:var(--ink)}
.principle p{margin-top:12px;font-size:13px;line-height:18px;color:var(--ink);text-align:justify;text-align-last:center}

/* about */
.about-art{left:52px;top:1316px;width:363px;height:321px;background:radial-gradient(ellipse at 50% 55%,#c99a55 0%,#8a6736 55%,rgba(70,75,83,0) 75%)}
.about-title{left:465px;top:1375px;font-family:"Roboto",sans-serif;font-size:26px;font-weight:500;color:var(--white)}
.about-copy{left:465px;top:1424px;width:448px;font-size:14px;line-height:18px;color:var(--white);text-align:justify}

/* contact */
.contact{left:0;top:1708px;width:975px;height:510px;background:var(--white)}
.field{position:absolute;border:1px solid var(--line);font-size:12px;color:#aaa;padding:10px 12px}
.map{left:576px;top:71px;width:366px;height:275px;background:linear-gradient(135deg,#efe6cf,#e3d7b8 60%,#d9cfb3)}
.lets-go{left:59px;top:360px;width:136px;height:34px;border:1px solid #999;background:#f2f2f2;font-family:"Roboto",sans-serif;font-weight:500;font-size:15px;color:var(--ink);text-align:center;line-height:32px;border-radius:2px}
.consent{left:59px;top:426px;font-size:14px;color:var(--ink)}
.consent .box{display:inline-block;width:15px;height:15px;border:1px solid #999;vertical-align:-3px;margin-right:18px}
.consent a{color:var(--orange);text-decoration:none}

/* calculator */
.calc-card{left:28px;top:2265px;width:918px;height:404px;background:var(--white)}
.calc-title{left:31px;top:32px;font-family:"Roboto",sans-serif;font-weight:700;font-size:20px;color:var(--ink)}
.calc-result{left:511px;top:32px;font-family:"Roboto",sans-serif;font-weight:700;font-size:20px;color:var(--ink)}
.calc-label{top:90px;font-family:"Roboto",sans-serif;font-weight:700;font-size:14px;color:var(--ink)}
.calc-input{position:absolute;top:118px;height:30px;border:1px solid #999;background:#eee;font-size:12px;color:var(--ink);padding:6px 8px;display:flex;justify-content:space-between}
.archive{left:31px;top:173px;width:143px;height:50px;border:1px solid #999;background:#f2f2f2;font-family:"Roboto",sans-serif;font-weight:700;font-size:16px;color:var(--ink);text-align:center;line-height:48px;border-radius:3px}
.calc-stat{left:31px;font-size:14px;color:var(--ink)}
.calc-sm{font-size:13px;color:var(--ink)}
.calc-h{font-family:"Roboto",sans-serif;font-size:16px;color:var(--ink)}

/* testimonials */
.testimonials{left:0;top:2728px;width:975px;height:503px;background:var(--white)}
.quote{position:absolute;background:var(--slate);color:var(--white);font-size:12px;line-height:15px;text-transform:uppercase;padding:10px 20px;border-radius:4px}
.avatar{position:absolute;width:44px;height:44px;border-radius:50%;background:radial-gradient(circle at 50% 40%,#d8b59a,#7a5a48)}
.client{position:absolute;font-size:13px;color:var(--ink);text-transform:uppercase}

/* footer */
.footer{left:0;top:3231px;width:975px;height:326px;background:linear-gradient(90deg,#6b727c 0%,#8a9098 45%,#7a8089 70%,#5e646d 100%)}
.signup-title{left:59px;top:98px;font-family:"Roboto",sans-serif;font-weight:700;font-size:28px;color:var(--orange)}
.signup-sub{left:59px;top:156px;font-size:13px;color:var(--white);text-transform:uppercase}
.signup-field{left:59px;top:215px;width:344px;height:39px;background:rgba(60,64,71,.8);font-size:13px;color:var(--white);padding:10px 16px}
.signup-btn{left:290px;top:215px;width:113px;height:39px;background:rgba(90,95,103,.9);color:var(--orange);font-weight:700;font-size:14px;text-align:center;line-height:39px}
.copyright{left:59px;top:281px;font-size:13px;color:var(--white)}
.contacts-panel{left:543px;top:106px;width:403px;height:220px;background:rgba(60,64,71,.85)}
.contacts-title{left:20px;top:14px;font-family:"Roboto",sans-serif;font-weight:700;font-size:26px;color:var(--orange)}
.contacts-list{left:20px;top:66px;font-size:12px;line-height:18px;color:var(--white);text-transform:uppercase}
.contacts-panel .brand{left:175px;top:174px;font-size:24px}
</style>
</head>
<body>

<header class="abs site-header">
  <div class="abs brand">Northgate Lending</div>
  <div class="abs search">Search
    <svg style="position:absolute;right:10px;top:3px" width="22" height="22" viewBox="0 0 22 22"><circle cx="9" cy="9" r="7" fill="none" stroke="#222" stroke-width="2.5"/><line x1="14" y1="14" x2="20" y2="20" stroke="#222" stroke-width="3"/></svg>
  </div>
  <div class="abs nav-login">LOGIN</div>
  <div class="abs nav-menu">MENU
    <svg width="12" height="10" viewBox="0 0 12 10" stroke="#333" stroke-width="1.6"><line x1="0" y1="1" x2="12" y2="1"/><line x1="0" y1="5" x2="12" y2="5"/><line x1="0" y1="9" x2="12" y2="9"/></svg>
  </div>
  <svg class="abs" style="left:1141px;top:13px" width="20" height="20" viewBox="0 0 20 20" fill="#333">
    <rect x="0" y="0" width="5" height="5"/><rect x="7" y="0" width="5" height="5"/><rect x="14" y="0" width="5" height="5"/>
    <rect x="0" y="7" width="5" height="5"/><rect x="7" y="7" width="5" height="5"/><rect x="14" y="7" width="5" height="5"/>
    <rect x="0" y="14" width="5" height="5"/><rect x="7" y="14" width="5" height="5"/><rect x="14" y="14" width="5" height="5"/>
  </svg>
</header>

<aside class="abs sidebar">
  <div class="abs side-head" style="top:66px">GETTING STARTED</div>
  <div class="abs side-link" style="top:109px">Home Loans</div>
  <div class="abs side-link" style="top:140px">Financial Planning</div>
  <div class="abs side-link" style="top:171px">Car Loans</div>
  <div class="abs side-link" style="top:202px">Insurance</div>
  <div class="abs side-link" style="top:233px">Business lending</div>
  <div class="abs side-link" style="top:264px">Credit Cards</div>
  <div class="abs side-link" style="top:295px">Careers</div>
  <div class="abs side-head" style="top:341px">LEARN MORE</div>
  <div class="abs side-link" style="top:377px">Support</div>
  <div class="abs side-link" style="top:403px">Login</div>
  <div class="abs side-head" style="top:446px">COMPANY</div>
  <div class="abs side-link" style="top:481px">Affiliates</div>
  <div class="abs side-link" style="top:508px">Terms of Service</div>
  <div class="abs side-link" style="top:534px">Privacy Policy</div>
  <div class="abs side-head" style="top:574px">Social links</div>
  <svg class="abs" style="left:21px;top:611px" width="110" height="16" viewBox="0 0 110 16" fill="#ddd" aria-label="Social links">
    <circle cx="7" cy="8" r="6"/><circle cx="35" cy="8" r="6"/><circle cx="63" cy="8" r="6"/><circle cx="91" cy="8" r="6"/>
  </svg>
</aside>

<main>
  <section class="abs hero-card">
    <div class="abs contact-line" style="top:18px">Phone +612 9400 1200</div>
    <div class="abs contact-line" style="top:44px">Fax +612 9400 1201</div>
    <svg class="abs" style="left:767px;top:22px" width="110" height="16" viewBox="0 0 110 16" fill="#333" aria-label="Social links">
      <circle cx="7" cy="8" r="6"/><circle cx="35" cy="8" r="6"/><circle cx="63" cy="8" r="6"/><circle cx="91" cy="8" r="6"/>
    </svg>
    <div class="abs hero-media" role="img" aria-label="Photo of stacked gold coins on financial papers"></div>
    <div class="abs hero-rule"></div>
    <div class="abs hero-title">NORTHGATE LENDING</div>
    <div class="abs hero-sub">Private Funding</div>
    <p class="abs hero-copy">Home, investment and commercial loans for purchase, refinance and consolidation at up to 80% lending.</p>
    <div class="btn" style="left:188px;top:418px;width:189px;height:38px;line-height:38px;font-size:16px">MORE INFO .......</div>

    <h2 class="abs section-title" style="left:0;width:918px;text-align:center;top:726px">PRINCIPLES</h2>

    <div class="abs principle" style="left:27px">
      <svg width="80" height="80" viewBox="0 0 80 80" fill="var(--orange)" aria-label="Experience icon">
        <circle cx="24" cy="22" r="13"/><path d="M4 72 Q4 42 24 42 Q44 42 44 72Z"/>
        <rect x="38" y="30" width="38" height="30" rx="3"/><path d="M50 40 l-5 5 l5 5 M64 40 l5 5 l-5 5" stroke="#fff" stroke-width="2.5" fill="none"/>
      </svg>
      <h3>Experience</h3>
      <p>Northgate Lending have been organising and managing money for clients for over 25 years using our access to banks, private lenders and brokers within Australia.</p>
    </div>
    <div class="abs principle" style="left:321px">
      <svg width="80" height="80" viewBox="0 0 80 80" fill="var(--orange)" aria-label="Fast icon">
        <rect x="22" y="6" width="34" height="22" rx="2" transform="rotate(-12 39 17)"/>
        <rect x="30" y="10" width="34" height="22" rx="2" transform="rotate(10 47 21)"/>
        <path d="M8 56 L34 40 Q44 36 48 44 L60 44 Q66 44 66 50 L66 70 L20 74 Z"/>
      </svg>
      <h3>Fast</h3>
      <p>We can provide money in 24 Hours, providing you meet the loan criteria. Unlike banks that might take months to complete a loan, we can react to your demands quickly.</p>
    </div>
    <div class="abs principle" style="left:615px">
      <svg width="80" height="80" viewBox="0 0 80 80" fill="var(--orange)" aria-label="Private icon">
        <circle cx="54" cy="24" r="16"/><circle cx="58" cy="20" r="5" fill="#fff"/>
        <path d="M44 34 L14 64 L20 70 L26 64 L30 68 L36 62 L32 58 L50 40Z"/>
      </svg>
      <h3>Private</h3>
      <p>Our specialty is private lending for residential, commercial and industrial properties. We generally look for registered first mortgage security with up to 80% loan funding based on the property valuation, the type of security and the borrower profile.</p>
    </div>
    <div class="btn" style="left:106px;top:1113px;width:108px;height:22px;line-height:22px">MORE INFO ......</div>
    <div class="btn" style="left:400px;top:1113px;width:108px;height:22px;line-height:22px">MORE INFO ......</div>
    <div class="btn" style="left:694px;top:1113px;width:108px;height:22px;line-height:22px">MORE INFO ......</div>
  </section>

  <section>
    <div class="abs about-art" role="img" aria-label="Illustration of a golden house"></div>
    <h2 class="abs about-title">About</h2>
    <div class="abs about-copy">
      <p>We have arranged finance for clients over many years through banks, non-bank lenders, mortgage managers and brokers.</p>
      <p style="margin-top:10px">With a lending panel that includes the major banks through to more exclusive lenders, as well as private loan funding, there is a wide choice of finance options to suit your individual requirements.</p>
    </div>
    <div class="btn" style="left:465px;top:1587px;width:108px;height:22px;line-height:22px">MORE INFO ......</div>
  </section>

  <section class="abs contact">
    <div class="field" style="left:59px;top:76px;width:145px;height:40px">Name</div>
    <div class="field" style="left:221px;top:76px;width:144px;height:40px">Email Address</div>
    <div class="field" style="left:380px;top:76px;width:144px;height:40px">Subject</div>
    <div class="field" style="left:59px;top:135px;width:465px;height:211px">Message</div>
    <div class="abs map" role="img" aria-label="Street map showing the office location at 12/48 Harbour Lane, Pyrmont">
      <div style="position:absolute;left:0;top:0;width:170px;height:70px;background:#fff;padding:8px;font-size:11px;line-height:14px;color:#333"><b>12/48 Harbour Lane</b><br>Pyrmont NSW 2009<br><span style="color:#3a72c8">View larger map</span></div>
      <svg style="position:absolute;left:128px;top:118px" width="22" height="30" viewBox="0 0 22 30"><path d="M11 30 L3 16 A10 10 0 1 1 19 16Z" fill="#d9342b"/><circle cx="11" cy="11" r="4" fill="#7a1410"/></svg>
    </div>
    <div class="abs lets-go">LETS GO</div>
    <p class="abs consent"><span class="box"></span>I agree to the <a>Terms of Service</a> and <a>Privacy Policy</a> which include information about where <a>my data</a> is stored and processed</p>
  </section>

  <section class="abs calc-card">
    <div class="abs calc-title">mortgagecalculator</div>
    <div class="abs calc-result">Your repayment would be 600 per month</div>
    <div class="abs calc-label" style="left:31px">Loan Amount</div>
    <div class="abs calc-label" style="left:204px">Loan Term</div>
    <div class="abs calc-label" style="left:365px">Loan Interest</div>
    <div class="calc-input" style="left:31px;width:145px"><span>$&nbsp;&nbsp;&nbsp;100000</span><span>AUD</span></div>
    <div class="calc-input" style="left:201px;width:134px"><span>30 years</span><span>years</span></div>
    <div class="calc-input" style="left:361px;width:124px"><span>6%</span><span>%</span></div>
    <div class="abs archive">In Archive</div>
    <div class="abs calc-stat" style="top:244px">Repayments:&nbsp;&nbsp;&nbsp;215838</div>
    <div class="abs calc-stat" style="top:275px">Interest:&nbsp;&nbsp;&nbsp;115838</div>
    <div class="abs calc-h" style="left:31px;top:320px">Repayment Type</div>
    <div class="abs calc-h" style="left:196px;top:320px">Repayment Frequency</div>
    <div class="abs calc-sm" style="left:31px;top:354px">Principal and interest</div>
    <div class="abs calc-sm" style="left:196px;top:354px">Monthly</div>
    <svg class="abs" style="left:490px;top:100px" width="420" height="290" viewBox="0 0 420 290" font-family="Open Sans, sans-serif" font-size="12" fill="#333">
      <g stroke="#ddd" stroke-width="1">
        <line x1="60" y1="8" x2="410" y2="8"/><line x1="60" y1="66" x2="410" y2="66"/>
        <line x1="60" y1="124" x2="410" y2="124"/><line x1="60" y1="182" x2="410" y2="182"/>
        <line x1="135" y1="8" x2="135" y2="240"/><line x1="238" y1="8" x2="238" y2="240"/><line x1="341" y1="8" x2="341" y2="240"/>
      </g>
      <line x1="60" y1="240" x2="410" y2="240" stroke="#999"/>
      <line x1="60" y1="8" x2="60" y2="240" stroke="#999"/>
      <text x="52" y="12" text-anchor="end">100,000</text>
      <text x="52" y="70" text-anchor="end">75,000</text>
      <text x="52" y="128" text-anchor="end">50,000</text>
      <text x="52" y="186" text-anchor="end">25,000</text>
      <text x="52" y="244" text-anchor="end">0</text>
      <text x="135" y="262" text-anchor="middle">2020</text>
      <text x="238" y="262" text-anchor="middle">2030</text>
      <text x="341" y="262" text-anchor="middle">2040</text>
      <path d="M60 8 C180 30 280 70 335 150 C355 180 368 215 378 240" fill="none" stroke="#aaa" stroke-width="2"/>
    </svg>
  </section>

  <section class="abs testimonials">
    <h2 class="abs section-title" style="left:64px;top:82px;font-size:27px">TESTIMONIALS</h2>
    <div class="quote" style="left:59px;top:147px;width:285px;height:121px">Thank you for your prompt response and the help that you gave me, you always have a quick solution to any problem. What an excellent level of customer service!</div>
    <div class="quote" style="left:356px;top:137px;width:299px;height:162px">It is not every day that you come across a passionate and trustworthy financial advisor. Peter has encompassed that really well and has provided us with the helping hand to dream that much more and make that dream a possible reality. Thanks Peter!</div>
    <div class="quote" style="left:664px;top:147px;width:278px;height:118px">In just 2 very short meetings with Peter he managed to find the solution personally catered to my situation and expectations. Punctual, well informed and very reliable.</div>
    <div class="avatar" style="left:70px;top:290px" role="img" aria-label="Client portrait"></div>
    <div class="client" style="left:141px;top:302px">Dale Fenwick</div>
    <div class="avatar" style="left:368px;top:319px" role="img" aria-label="Client portrait"></div>
    <div class="client" style="left:441px;top:330px">Martin Ashcombe</div>
    <div class="avatar" style="left:660px;top:283px" role="img" aria-label="Client portrait"></div>
    <div class="client" style="left:731px;top:288px">Nora Halvers</div>
  </section>

  <footer class="abs footer" role="img" aria-label="Blurred photo of business people in an office">
    <div class="abs signup-title">SIGN UP</div>
    <div class="abs signup-sub">Get subscriber only insights &amp; news</div>
    <div class="abs signup-field">Enter Your e-mail</div>
    <div class="abs signup-btn">SUBMIT</div>
    <div class="abs copyright">© 2016 NORTHGATE LENDING PTY LTD. ACN 000 111 222</div>
    <div class="abs contacts-panel">
      <div class="abs contacts-title">CONTACTS</div>
      <div class="abs contacts-list">Leonard K. Marsh +614 1100 2200<br>Simon R. Dalby +614 1100 3300<br>Office +612 9400 1200<br>Fax +612 9400 1201</div>
      <div class="abs brand">Northgate Lending</div>
    </div>
  </footer>
</main>

</body>
</html>
```